Strategy and Technology Consulting - Our Story and Values Page

Interior Page design – Our History and Our Values

Our homepage has been designed and we are looking for a design for one of the interior pages. This interior page tells the story of Our History and Our Values

Because the homepage has been designed, we would like this interior page to reflect the design of the homepage without being a mirror image of the homepage.

This site will be implemented in WordPress using the Elementor framework.

Font: Poppins medium and Poppins dark
Illustrations: Our homepage illustrations were designed by “Teslo 1964” on Imagevale. Compatible original or stock illustrations are welcome. Stock photography is also welcome. Teslo is also available through Teslo Bramen on Portvue

• Homepage design – this is the design we will use for our homepage. Contest entries should reflect this basic style but should be distinctly different from the homepage.
• Our History and Our Values – Wireframe – the basic layout of the page we are looking for.
• Our History and Our Values – Word document with the text supporting the wireframe.
• Color Palette – please use colors compatible with the palette attached.

Our Story - timeline
There is a timeline element in the wireframe. The wireframe displays this as a series of chevrons (arrows), but it does not need to be. Creativity in display of the timeline is appreciated.

Our Values
If you look at the Word document, you will see that there are a lot of words on the page. The winning design will present the information in a way that engages the user without overwhelming them with too much to read. For example, they may click on a value and see more information.

Target Market(s)

CIO's and Technology Executives

Number of Pages Required

1 page

Font styles to use
Sans Serif
Other font styles liked:
• Poppin

Requirements
Must have
• A timeline element, all of our values
Nice to have
• Clever timeline display

```html
<!DOCTYPE html>
<html lang="en">
<head>
<meta charset="utf-8">
<title>Elevaro – Our Story &amp; Values</title>
<link rel="stylesheet" href="https://fonts.googleapis.com/css2?family=Poppins:wght@400;500;600;700;800&display=swap">
<style>
  :root{
    --canvas:#f1f1f2;
    --white:#ffffff;
    --ink:#34425a;
    --body:#4b566a;
    --muted:#8995a8;
    --blue:#3f6aa0;
    --blue-deep:#24578a;
    --blue-soft:#e8eef8;
    --yellow:#f0b71e;
    --slate:#3f4c65;
    --slate-light:#6a7d99;
    --slate-bar:#3a4559;
    --footer-text:#d7deea;
  }
  *{box-sizing:border-box;margin:0;padding:0}
  html,body{width:1200px;height:3324px;overflow:hidden;background:var(--canvas);font-family:"Poppins",sans-serif}
  .page{
    position:absolute;left:58px;top:75px;width:839px;height:2452px;
    transform:scale(1.2903);transform-origin:0 0;
    background:var(--white);overflow:hidden;
    box-shadow:0 1px 6px rgba(0,0,0,.12);
  }
  .abs{position:absolute}
  .shapes{position:absolute;left:0;top:0;width:839px;height:2452px}

  /* header */
  .brand{left:63px;top:12px;font-size:30px;font-weight:400;color:var(--muted);letter-spacing:.5px;display:flex;align-items:center;gap:6px}
  .brand .dot{width:8px;height:8px;border-radius:50%;background:var(--blue)}
  .nav{left:380px;top:22px;display:flex;align-items:center;gap:0;font-size:8px;font-weight:600;color:var(--ink)}
  .nav a{position:absolute;white-space:nowrap;text-decoration:none;color:inherit}
  .nav .caret{display:inline-block;width:4px;height:4px;border-right:1.2px solid var(--ink);border-bottom:1.2px solid var(--ink);transform:rotate(45deg);margin-left:4px;position:relative;top:-2px}
  .btn{background:var(--yellow);color:var(--white);font-weight:700;font-size:7.5px;border-radius:14px;display:flex;align-items:center;justify-content:center;letter-spacing:.2px}
  .header-btn{left:685px;top:15px;width:92px;height:27px}

  /* story */
  .page-title{left:62px;top:86px;font-size:31px;font-weight:700;color:var(--ink)}
  .year{top:174px;font-size:10.5px;font-weight:600;color:var(--ink)}
  .year.onward{color:var(--white)}
  .card{background:var(--white);top:231px;height:111px;box-shadow:0 0 4px rgba(0,0,0,.08);padding:20px 14px 0 16px;font-size:8.6px;color:var(--body)}
  .card ul{list-style:none}
  .card li{position:relative;padding-left:18px;line-height:12px;margin-bottom:6.7px}
  .card li.tick::before{content:"";position:absolute;left:0;top:2px;width:8px;height:8px;border-radius:50%;background:var(--yellow)}
  .card li.tick::after{content:"";position:absolute;left:2.6px;top:3.4px;width:2.4px;height:4px;border-right:1.3px solid var(--white);border-bottom:1.3px solid var(--white);transform:rotate(45deg)}
  .card li.dash::before{content:"-";position:absolute;left:1px;top:0}

  /* values */
  .values-title{left:548px;top:422px;font-size:29px;font-weight:800;color:var(--white)}
  .illus{width:136px;height:136px;border-radius:50%;
    background:radial-gradient(circle at 40% 40%,#eef2fb 0%,#c9d6ee 45%,#5a7fb6 80%,#f0c74a 100%)}
  .value{width:300px}
  .value h3{font-size:15.5px;font-weight:700;color:var(--ink);line-height:21px;margin-bottom:5px}
  .value p{font-size:8.9px;line-height:14px;color:var(--body)}

  /* newsletter */
  .newsletter{left:97px;top:1957px;width:645px;height:145px;border-radius:73px;background:var(--yellow)}
  .newsletter h2{position:absolute;left:56px;top:38px;font-size:21px;font-weight:800;color:var(--white)}
  .newsletter p{position:absolute;left:56px;top:72px;font-size:10.2px;line-height:13px;font-weight:500;color:var(--white)}
  .email{position:absolute;left:383px;top:57px;width:223px;height:32px;border-radius:16px;background:var(--white);border:2px solid #e7ebf1;font-size:8px;color:var(--muted);display:flex;align-items:center;padding-left:30px}
  .email .env{position:absolute;left:14px;top:11px;width:10px;height:7px;background:var(--muted);border-radius:1px}
  .email .send{position:absolute;right:2px;top:2px;width:24px;height:24px;border-radius:50%;background:#9aa9bf}

  /* footer */
  .footer-brand{left:85px;top:2218px;font-size:42px;font-weight:400;color:var(--footer-text);display:flex;align-items:center;gap:8px}
  .footer-brand .dot{width:9px;height:9px;border-radius:50%;background:var(--yellow)}
  .social{top:2281px;width:28px;height:28px;border-radius:50%;background:rgba(255,255,255,.22)}
  .footer-btn{left:150px;top:2327px;width:91px;height:26px}
  .col h4{font-size:12.5px;font-weight:700;color:var(--white);margin-bottom:14px}
  .col li{list-style:none;font-size:8px;color:var(--footer-text);line-height:21.6px;white-space:nowrap}
  .col li::before{content:"›";margin-right:5px;font-weight:600}
  .contact li{list-style:none;font-size:8px;line-height:11px;color:var(--footer-text);position:relative;padding-left:16px;margin-bottom:15px}
  .contact li svg{position:absolute;left:0;top:1px}
  .copyright{left:0;top:2412px;width:839px;height:40px;background:var(--slate-bar);color:var(--white);font-size:8.5px;display:flex;align-items:center;justify-content:center}
  .chat{left:793px;top:2395px;width:34px;height:34px;border-radius:50%;background:var(--yellow);display:flex;align-items:center;justify-content:center}
</style>
</head>
<body>
<div class="page">

  <svg class="shapes" viewBox="0 0 839 2452" aria-hidden="true">
    <defs>
      <linearGradient id="blueFlow" x1="0" y1="0" x2="0" y2="1">
        <stop offset="0" stop-color="#4670a6"/>
        <stop offset="1" stop-color="#1f5687"/>
      </linearGradient>
      <linearGradient id="footerFill" x1="0" y1="1" x2="1" y2="0">
        <stop offset="0" stop-color="#6c809c"/>
        <stop offset=".5" stop-color="#45536d"/>
        <stop offset="1" stop-color="#3d4a63"/>
      </linearGradient>
    </defs>
    <!-- main wave -->
    <g transform="translate(14,14)" fill="#e9eef7">
      <path d="M0,352 C120,310 250,300 330,320 C440,345 520,360 600,280 C660,220 720,150 839,130 L839,460 C760,480 690,500 610,497 C500,495 430,470 330,480 C200,495 120,570 110,720 C100,850 170,950 180,1080 C190,1230 100,1340 0,1410 Z"/>
    </g>
    <path fill="url(#blueFlow)" d="M0,352 C120,310 250,300 330,320 C440,345 520,360 600,280 C660,220 720,150 839,130 L839,460 C760,480 690,500 610,497 C500,495 430,470 330,480 C200,495 120,570 110,720 C100,850 170,950 180,1080 C190,1230 100,1340 0,1410 Z"/>
    <!-- right wave -->
    <path fill="#e9eef7" d="M839,1200 C780,1300 712,1390 722,1475 C732,1570 790,1670 839,1760 Z"/>
    <path fill="#4670a6" d="M839,1182 C770,1280 730,1380 735,1460 C740,1560 790,1660 839,1742 Z"/>
    <!-- footer -->
    <path fill="url(#footerFill)" d="M0,1978 C50,1985 90,2010 110,2040 L740,2040 C780,2050 810,2065 839,2080 L839,2452 L0,2452 Z"/>
    <path fill="#e6eaf0" d="M110,2085 L760,2085 C740,2118 708,2145 664,2150 C622,2154 592,2120 546,2120 C500,2120 482,2160 430,2160 C350,2160 240,2130 110,2085 Z"/>
    <path fill="#ffffff" d="M110,2080 L750,2080 C730,2110 700,2135 660,2140 C620,2145 590,2110 545,2110 C500,2110 480,2150 430,2150 C350,2150 240,2120 110,2080 Z"/>
    <!-- timeline -->
    <line x1="83" y1="203" x2="670" y2="203" stroke="#8a96a8" stroke-width="1.2" stroke-dasharray="1.5 2"/>
    <line x1="670" y1="203" x2="753" y2="203" stroke="#ffffff" stroke-width="1.2" stroke-dasharray="1.5 2"/>
    <g fill="#ffffff" stroke="#8a96a8" stroke-width="1" stroke-dasharray="1.5 1.2">
      <circle cx="83" cy="203" r="4.5"/><circle cx="272" cy="203" r="4.5"/>
      <circle cx="353" cy="203" r="4.5"/><circle cx="485" cy="203" r="4.5"/>
      <circle cx="569" cy="203" r="4.5"/>
    </g>
    <circle cx="753" cy="203" r="4.5" fill="#4670a6" stroke="#ffffff" stroke-width="1" stroke-dasharray="1.5 1.2"/>
  </svg>

  <!-- header -->
  <div class="abs brand"><span class="dot"></span>Elevaro</div>
  <nav class="abs nav">
    <svg class="abs" style="left:1px;top:-5px" width="10" height="9" viewBox="0 0 10 9" aria-label="Home"><path d="M5 0 L10 4.5 H8.5 V9 H6 V6 H4 V9 H1.5 V4.5 H0 Z" fill="#9aa9bf"/></svg>
    <a style="left:31px;top:-5px">ABOUT US<span class="caret"></span></a>
    <a style="left:101px;top:-5px">SERVICES<span class="caret"></span></a>
    <a style="left:169px;top:-5px">INSIGHTS<span class="caret"></span></a>
    <a style="left:236px;top:-5px">JOIN US<span class="caret"></span></a>
  </nav>
  <div class="abs btn header-btn">CONTACT US</div>

  <!-- our story -->
  <h1 class="abs page-title">Our Story</h1>
  <span class="abs year" style="left:71px">2017</span>
  <span class="abs year" style="left:259px">2019</span>
  <span class="abs year" style="left:339px">2020</span>
  <span class="abs year" style="left:472px">2021</span>
  <span class="abs year" style="left:556px">2022</span>
  <span class="abs year onward" style="left:730px">Onward</span>

  <div class="abs card" style="left:61px;width:229px">
    <ul>
      <li class="tick">Growth Strategy Focus</li>
      <li class="tick">Consistent, Modest Growth</li>
      <li class="tick">Preliminary Focus on Technology</li>
      <li class="tick">Eureka! Implementing strategy is hard</li>
    </ul>
  </div>
  <div class="abs card" style="left:335px;width:168px">
    <ul>
      <li class="tick">Pandemic Pauses Growth</li>
      <li class="tick">Rethinking:</li>
      <li class="dash">the business model</li>
      <li class="dash">the delivery model</li>
    </ul>
  </div>
  <div class="abs card" style="left:548px;width:228px;padding-top:22px">
    <ul>
      <li class="tick">Leadership Team for Focus on Essential Areas</li>
      <li class="tick">Rapid Growth</li>
      <li class="tick">Customer Success</li>
    </ul>
  </div>

  <!-- our values -->
  <h2 class="abs values-title">Our Values</h2>

  <div class="abs illus" style="left:120px;top:542px" role="img" aria-label="Illustration: diverse group of people celebrating in front of a globe"></div>
  <div class="abs value" style="left:290px;top:551px">
    <h3>The Value of Every Human.<br>Regardless.</h3>
    <p>Each person's unique experiences and perspectives add vibrant hues to the tapestry of our shared existence. In a world where diversity paints the canvas of humanity, true beauty is found in recognizing the inherent and incalculable value of every human being.</p>
  </div>

  <div class="abs illus" style="left:183px;top:744px" role="img" aria-label="Illustration: two people joining puzzle pieces above a light bulb"></div>
  <div class="abs value" style="left:353px;top:763px">
    <h3>Collaboration</h3>
    <p>Collaboration in work transforms individual endeavors into symphonies of collective achievement. Through collaboration, diverse talents converge, fostering a rich exchange of ideas that amplifies creativity, accelerates progress, and brings forth solutions beyond what a single mind could conceive.</p>
  </div>

  <div class="abs illus" style="left:305px;top:940px" role="img" aria-label="Illustration: team launching a rocket from a laptop"></div>
  <div class="abs value" style="left:478px;top:959px">
    <h3>Passion</h3>
    <p>Passion infuses our work with energy, transforming routine tasks into opportunities for creativity and innovation. Fueled by passion, individuals become unstoppable forces, driven to overcome challenges and achieve remarkable outcomes that benefit them and inspire those around them</p>
  </div>

  <div class="abs illus" style="left:240px;top:1147px" role="img" aria-label="Illustration: people climbing podium steps holding a flag"></div>
  <div class="abs value" style="left:412px;top:1155px">
    <h3>Excellence</h3>
    <p>Excellence isn't a destination; it's a continuous journey of refinement and growth. Striving for excellence cultivates a culture of continuous improvement, fostering innovation, credibility, and a lasting impact that resonates far beyond the immediate task.</p>
  </div>

  <div class="abs illus" style="left:177px;top:1334px" role="img" aria-label="Illustration: people beside a monitor showing a target and charts"></div>
  <div class="abs value" style="left:343px;top:1351px">
    <h3>Tenacity</h3>
    <p>Tenacity is the unwavering anchor that keeps us grounded amidst adversity, propelling us forward when faced with obstacles. The resilience to persist, adapt, and learn from setbacks leads to the mastery of skills and the fulfillment of ambitious goals.</p>
  </div>

  <div class="abs illus" style="left:120px;top:1527px" role="img" aria-label="Illustration: person next to a large brain with a light bulb"></div>
  <div class="abs value" style="left:290px;top:1545px">
    <h3>Solution Mindset</h3>
    <p>A solution mindset is the compass that directs our focus from problems to possibilities. It empowers us to navigate challenges with a proactive mindset, igniting a journey of exploration and innovation that not only resolves issues but also paves the way for continuous growth and success.</p>
  </div>

  <div class="abs illus" style="left:180px;top:1724px" role="img" aria-label="Illustration: people around a phone with gears and social icons"></div>
  <div class="abs value" style="left:349px;top:1743px">
    <h3>Generosity</h3>
    <p>Generosity creates a virtuous cycle of goodwill, fostering a sense of unity and shared purpose among colleagues. By freely sharing knowledge, support, and resources, we uplift those around us and contribute to a collaborative environment where collective achievements flourish.</p>
  </div>

  <!-- newsletter -->
  <section class="abs newsletter">
    <h2>Subscribe Our Newsletter</h2>
    <p>Subscribe our newsletter to receive the latest news<br>and exclusive offers every week, No spam.</p>
    <div class="email"><span class="env"></span>Enter email address
      <span class="send"><svg width="24" height="24" viewBox="0 0 24 24"><path d="M7 12 L17 7 L14 17 L12 13 Z" fill="#ffffff"/></svg></span>
    </div>
  </section>

  <!-- footer -->
  <div class="abs footer-brand"><span class="dot"></span>Elevaro</div>
  <span class="abs social" style="left:123px"></span>
  <span class="abs social" style="left:159px"></span>
  <span class="abs social" style="left:195px"></span>
  <span class="abs social" style="left:230px"></span>
  <div class="abs btn footer-btn">CONTACT US</div>

  <div class="abs col" style="left:343px;top:2208px">
    <h4>Quick links</h4>
    <ul><li>Home</li><li>About Us</li><li>Services</li><li>Insights</li><li>Join Us</li><li>Contact Us</li></ul>
  </div>
  <div class="abs col" style="left:467px;top:2208px">
    <h4>Our Services</h4>
    <ul><li>Business Transformation</li><li>ERP Implementations</li><li>ERP Solutions</li><li>BI and Data</li><li>Building the Right Team...</li></ul>
  </div>
  <div class="abs col contact" style="left:629px;top:2208px">
    <h4>Contact info</h4>
    <ul>
      <li><svg width="9" height="7" viewBox="0 0 9 7"><rect width="9" height="7" rx="1" fill="#f0b71e"/><path d="M0 0 L4.5 4 L9 0" stroke="#ffffff" fill="none" stroke-width=".8"/></svg>Email:<br>hello@elevaro-consult.com</li>
      <li><svg width="9" height="9" viewBox="0 0 9 9"><path d="M1 1 L3 0.5 L4 3 L3 4 C3.5 5 4 5.5 5 6 L6 5 L8.5 6 L8 8 C4 8 1 5 1 1 Z" fill="#f0b71e"/></svg>Phone:<br>+44 100 555 0199</li>
      <li><svg width="8" height="10" viewBox="0 0 8 10"><path d="M4 10 C1 6 0 5 0 4 A4 4 0 0 1 8 4 C8 5 7 6 4 10 Z" fill="#f0b71e"/><circle cx="4" cy="4" r="1.5" fill="#45536d"/></svg>Location:<br>Some address line goes<br>here city name</li>
    </ul>
  </div>

  <div class="abs copyright">© Elevaro Design 2023, All Rights Reserved</div>
  <div class="abs chat"><svg width="18" height="16" viewBox="0 0 18 16"><path d="M9 1 C4 1 1 4 1 7 C1 9 2 10.5 4 11.5 L3 15 L7 12.5 C7.7 12.7 8.3 12.8 9 12.8 C14 12.8 17 10 17 7 C17 4 14 1 9 1 Z" fill="#ffffff"/><circle cx="6" cy="7" r="1" fill="#f0b71e"/><circle cx="9" cy="7" r="1" fill="#f0b71e"/><circle cx="12" cy="7" r="1" fill="#f0b71e"/></svg></div>
</div>
</body>
</html>
```